apparel brand store for hero type shirt

we need a website design for a new apparel compagny basend in montreal called '' ateliervoransol '' . We design innovative yet simple artwork for the city .we would like to get a MINIMALISTE soft color website . The design most communicate ' MUSUEM '' feeling.
simple looking but looking UPMARKET .
i dont have any exemple i really want you to focus on
( apparel + musuem looking + upmarket )

Requirements
Must have
• white backgroung with a little bit of ( orange / dark green and grey camo )
-the came as to be 5 to 10% transparant
Nice to have
• go fallow on ig
Should not have
• BRIGHT COLOURS

```html
<!DOCTYPE html>
<html lang="en">
<head>
<meta charset="utf-8">
<title>Ateliervoransol — Arts For Our City</title>
<link href="https://fonts.googleapis.com/css2?family=Playfair+Display:wght@400;700;900&family=Poppins:wght@300;400;500;600&display=swap" rel="stylesheet">
<style>
:root{
  --ink:#1e1e1e;
  --text:#555;
  --muted:#8f8f8f;
  --line:#e6e6e6;
  --tile:#f4f4f4;
  --sale:#e0582b;
  --cool:#2aa5d6;
  --star:#f2b01e;
  --band:#e9e9eb;
  --footer:#111111;
  --footer-text:#9a9a9a;
  --white:#ffffff;
  --clay:#d69168;
  --forest:#3d5645;
  --stone:#8d918b;
  --olive:#6d7358;
  --sand:#c9b69a;
}
*{box-sizing:border-box;margin:0;padding:0}
html,body{width:1200px;height:3671px;overflow:hidden}
body{position:relative;background:var(--white);font-family:'Poppins',sans-serif;color:var(--text)}
section,header,footer{position:absolute;left:0;width:1200px}

/* hero */
.hero{top:0;height:590px}
.hero-art{position:absolute;inset:0;background:
  radial-gradient(ellipse at 75% 40%,rgba(196,60,40,.85),transparent 55%),
  radial-gradient(ellipse at 30% 60%,rgba(40,70,130,.8),transparent 50%),
  radial-gradient(ellipse at 85% 80%,rgba(210,150,70,.7),transparent 45%),
  linear-gradient(180deg,#4d5a66 0%,#6b5646 45%,#8a4a36 100%)}
.hero-art::after{content:"";position:absolute;inset:0;background:rgba(0,0,0,.28)}
.nav{position:absolute;top:48px;left:48px;font-size:11px;color:var(--white);font-weight:500}
.nav span{position:absolute;white-space:nowrap}
.logo{font-family:'Playfair Display',serif;font-weight:700;color:var(--white);font-size:28px;letter-spacing:.2px}
.hero .logo{position:absolute;top:36px;left:0;width:1200px;text-align:center}
.nav-icons{position:absolute;top:48px;right:80px;display:flex;gap:20px}
.cart-count{position:absolute;top:-10px;left:24px;font-size:8px;color:var(--white)}
.hero-copy{position:absolute;top:258px;left:0;width:1200px;text-align:center;color:var(--white)}
.hero-copy h1{font-family:'Playfair Display',serif;font-weight:900;font-size:38px;letter-spacing:.3px}
.hero-copy p{font-size:13px;margin-top:6px;letter-spacing:.3px}
.btn-outline{display:inline-block;margin-top:40px;width:112px;height:36px;line-height:34px;border:1px solid var(--white);font-size:11px;color:var(--white)}
.torn{position:absolute;left:0;bottom:0;width:1200px;height:60px}

/* intro */
.intro{top:630px;text-align:center}
.eyebrow{font-size:9px;color:var(--muted)}
.section-title{font-family:'Playfair Display',serif;font-weight:700;font-size:19px;color:var(--ink)}
.anchor-rule{display:flex;align-items:center;justify-content:center;gap:10px;margin-top:18px}
.anchor-rule i{display:block;width:146px;height:1px;background:var(--line)}
.intro .lead{width:510px;margin:26px auto 0;font-size:10px;line-height:15px}
.signature{margin-top:30px;font-size:14px;font-weight:500;color:var(--ink);letter-spacing:1px}
.signature-role{font-size:10px;color:var(--muted);margin-top:2px}
.rule{position:absolute;left:231px;width:738px;height:1px;background:var(--line)}

/* products */
.products-head{top:940px;text-align:center}
.products-head p{width:440px;margin:10px auto 0;font-size:10px;line-height:15px}
.tabs{display:flex;justify-content:center;gap:22px;margin-top:32px;font-size:10px;font-weight:500;color:var(--ink)}
.grid{position:absolute;left:231px;display:grid;grid-template-columns:repeat(4,171px);column-gap:18.7px;row-gap:20px}
.product{height:260px}
.product-media{position:relative;height:170px;background:var(--tile);overflow:hidden}
.product-media::before{content:"";position:absolute;left:40px;top:28px;width:91px;height:114px;border-radius:6px;
  background:linear-gradient(160deg,var(--tone),var(--tone2,var(--tone)))}
.badge{position:absolute;z-index:1;top:14px;left:14px;width:32px;height:32px;border-radius:50%;background:var(--sale);color:var(--white);font-size:9px;line-height:32px;text-align:center;font-weight:500}
.badge.soft{background:#e7c5b2}
.product-meta{display:flex;justify-content:space-between;margin-top:14px;font-size:7px;color:var(--muted)}
.stars{color:var(--star);letter-spacing:1px;font-size:8px}
.product h3{font-weight:400;font-size:9px;color:#444;margin-top:10px;white-space:nowrap}
.price{font-size:10px;color:var(--muted);margin-top:10px}
.price s{margin-right:8px}
.price b{font-weight:500;color:var(--sale)}
.price b.cool{color:var(--cool)}

/* testimonial */
.testimonial{top:1660px;height:450px}
.testimonial-art{position:absolute;inset:0;background:
  radial-gradient(ellipse at 95% 25%,rgba(214,145,104,.55),transparent 28%),
  radial-gradient(ellipse at 5% 75%,rgba(214,145,104,.5),transparent 25%),
  radial-gradient(ellipse at 30% 30%,rgba(61,86,69,.08),transparent 20%),
  radial-gradient(ellipse at 70% 80%,rgba(61,86,69,.08),transparent 22%),
  radial-gradient(ellipse at 60% 20%,rgba(141,145,139,.09),transparent 20%),
  linear-gradient(180deg,#f5f4f2,#ecebea)}
.avatar{position:absolute;top:100px;left:556px;width:88px;height:88px;border-radius:50%;background:linear-gradient(160deg,#4a3b33,#b08a74)}
.quote{position:absolute;left:0;width:1200px;text-align:center;font-family:'Playfair Display',serif;font-weight:900;font-size:44px;line-height:44px;color:var(--ink)}
.testimonial p{position:absolute;top:267px;left:350px;width:500px;text-align:center;font-size:10px;line-height:15px}
.arrow{position:absolute;top:262px;width:30px;height:30px;border:1px solid #999;border-radius:50%}

/* latest */
.latest-head{top:2180px;text-align:center}
.latest-head p{font-size:10px;margin-top:8px}

/* promo */
.promo{top:2599px;height:391px;background:var(--band)}
.promo-art{position:absolute;left:150px;top:0;width:520px;height:391px;background:
  radial-gradient(ellipse at 25% 75%,rgba(232,205,190,.95),transparent 30%),
  radial-gradient(ellipse at 78% 72%,rgba(238,210,195,.95),transparent 28%),
  radial-gradient(ellipse at 55% 30%,rgba(110,75,50,.35),transparent 35%),
  linear-gradient(180deg,#ebebed,#e4e4e6)}
.promo-copy{position:absolute;left:731px;top:78px;width:300px}
.promo-copy h2{font-family:'Playfair Display',serif;font-weight:900;font-size:44px;color:var(--ink);line-height:1.1}
.promo-copy h3{font-weight:500;font-size:23px;color:var(--ink);letter-spacing:.5px;margin-top:6px}
.promo-copy p{font-size:10.5px;line-height:14px;color:#333;margin-top:18px;width:265px}
.btn-solid{display:block;width:174px;height:48px;line-height:48px;text-align:center;background:#050505;color:var(--white);font-size:15px;margin-top:36px}

/* features */
.features{top:3038px}
.feature{position:absolute;width:220px;text-align:center}
.feature h4{font-size:7.5px;font-weight:600;color:var(--ink);margin-top:10px}
.feature p{font-size:8.5px;line-height:14px;color:var(--muted);margin-top:10px}

/* newsletter */
.newsletter{top:3226px;text-align:center}
.newsletter .eyebrow{font-size:8px}
.newsletter h2{font-family:'Playfair Display',serif;font-weight:700;font-size:19px;color:var(--ink);margin-top:2px}
.newsletter p{width:410px;margin:6px auto 0;font-size:9px;line-height:15px}
.signup{position:absolute;top:107px;left:393px;width:414px;height:34px;border:1px solid var(--line);display:flex;font-size:7.5px}
.signup span{flex:1;text-align:left;padding-left:14px;line-height:32px;color:#bbb}
.signup b{width:120px;border-left:1px solid var(--line);line-height:32px;color:var(--ink);font-weight:600}

/* footer */
.site-footer{top:3393px;height:278px;background:var(--footer);color:var(--footer-text);font-size:8px}
.footer-rule{position:absolute;left:43px;width:1114px;height:1px;background:#2a2a2a}
.site-footer .logo{position:absolute;top:52px;left:232px;font-size:26px}
.about{position:absolute;top:100px;left:234px;width:190px;line-height:18px}
.social{position:absolute;top:146px;left:233px;display:flex;gap:7px}
.social i{display:block;width:22px;height:22px;border-radius:50%;background:#3a3a3a}
.col{position:absolute;top:62px}
.col h5{font-size:10px;color:var(--white);font-weight:500;margin-bottom:6px}
.col li{list-style:none;line-height:19.5px}
.col li svg{vertical-align:-2px;margin-right:8px}
.indent{padding-left:17px}
.copyright{position:absolute;top:222px;left:232px;font-size:9px;color:var(--white)}
.cards{position:absolute;top:222px;left:865px;display:flex;gap:5px}
.cards i{display:block;width:22px;height:13px;background:#d9d9d9;border-radius:2px}
</style>
</head>
<body>

<header class="hero">
  <div class="hero-art" role="img" aria-label="Large mosaic mural on a city building facade in red, blue and ochre tones"></div>
  <nav class="nav">
    <span style="left:0">Home</span>
    <span style="left:63px">Shop ▾</span>
    <span style="left:126px">Best Art</span>
    <span style="left:199px">Collections ▾</span>
    <span style="left:294px">Pages</span>
  </nav>
  <div class="logo">Ateliervoransol</div>
  <div class="nav-icons">
    <svg width="13" height="13" viewBox="0 0 13 13"><circle cx="5.5" cy="5.5" r="4" fill="none" stroke="#fff" stroke-width="1.8"/><path d="M8.5 8.5 12 12" stroke="#fff" stroke-width="2"/></svg>
    <span style="position:relative"><svg width="14" height="13" viewBox="0 0 14 13"><path d="M1 4h12l-2 8H3z" fill="#fff"/><path d="M4 4 7 0l3 4" fill="none" stroke="#fff" stroke-width="1.4"/></svg><span class="cart-count">0</span></span>
    <svg width="12" height="12" viewBox="0 0 12 12" fill="#fff"><rect y="1" width="12" height="2"/><rect y="5" width="12" height="2"/><rect y="9" width="12" height="2"/></svg>
  </div>
  <div class="hero-copy">
    <h1>We Craete Arts For Our City</h1>
    <p>Lorem ipsum dolor ait amet esta dimaria nuno valencia</p>
    <span class="btn-outline">Shop Now</span>
  </div>
  <svg class="torn" viewBox="0 0 1200 60" preserveAspectRatio="none"><path d="M0 20 L40 28 L80 18 L130 32 L170 22 L230 34 L290 26 L340 38 L400 30 L460 40 L520 34 L580 42 L640 36 L700 44 L760 30 L820 38 L880 28 L940 36 L1000 24 L1060 32 L1120 20 L1200 28 L1200 60 L0 60 Z" fill="#fff"/></svg>
</header>

<section class="intro">
  <div class="eyebrow">Who Are We</div>
  <h2 class="section-title">Welcome To Ateliervoransol</h2>
  <div class="anchor-rule"><i></i>
    <svg width="14" height="18" viewBox="0 0 14 18" fill="none" stroke="#555" stroke-width="1.2"><circle cx="7" cy="2.5" r="1.8"/><path d="M7 4.3V17M3 7h8M1 12c1 3 3 5 6 5s5-2 6-5"/></svg>
  <i></i></div>
  <p class="lead">Duis autem vel eum iriure dolor in hendrerit in vulputate velit esse molestie consequat, vel illum dolore eu feugiat nulla facilisis at vero eros et accumsan et iusto odio dignissim qui blandit praesent luptatum zzril delenit augue duis dolore te feugait nulla facilisi.</p>
  <div class="signature">ELISE MARCHAND</div>
  <div class="signature-role">CEO Ateliervoransol</div>
</section>
<div class="rule" style="top:888px"></div>

<section class="products-head">
  <h2 class="section-title">Popular Products</h2>
  <p>vulputate velit esse molestie consequat, vel illum dolore eu feugiat nulla facilisis at vero eros et accumsan et iusto odio dignissim.</p>
  <div class="tabs"><span>Handmade</span><span>Wood Art</span><span>Metal Art</span><span>Paintings</span></div>
</section>

<div class="grid" style="top:1089px">
  <article class="product"><div class="product-media" style="--tone:var(--forest);--tone2:#4c6a55" role="img" aria-label="Dark green hero graphic shirt, folded on a plain backdrop"></div><div class="product-meta"><span>Solvane</span><span class="stars">★★★★★</span></div><h3>Aopo Designs Hero Graphic Tee</h3><p class="price">$120.00</p></article>
  <article class="product"><div class="product-media" style="--tone:var(--clay);--tone2:#e2a27c" role="img" aria-label="Soft orange hero graphic shirt, folded"></div><div class="product-meta"><span>Solvane</span><span class="stars">★★★★★</span></div><h3>Copo Designs Hero Graphic Tee</h3><p class="price">$240.00</p></article>
  <article class="product"><div class="product-media" style="--tone:var(--stone);--tone2:#a4a7a1" role="img" aria-label="Grey camo hero shirt, folded"><span class="badge">-20%</span></div><div class="product-meta"><span>Solvane</span><span class="stars">★★★★★</span></div><h3>Eopo Designs Hero Graphic Tee</h3><p class="price"><s>$250.00</s><b>$200.00</b></p></article>
  <article class="product"><div class="product-media" style="--tone:var(--sand);--tone2:#ddd0bb" role="img" aria-label="Sand coloured city artwork shirt, folded"><span class="badge">-20%</span></div><div class="product-meta"><span>Solvane</span><span class="stars">★★★★★</span></div><h3>Gopo Designs Hero Graphic Tee</h3><p class="price"><s>$150.00</s><b>$120.00</b></p></article>
  <article class="product"><div class="product-media" style="--tone:var(--olive);--tone2:#868c70" role="img" aria-label="Olive camo hero shirt, folded"></div><div class="product-meta"><span>Solvane</span><span class="stars">★★★★★</span></div><h3>Bopo Designs Hero Graphic Tee</h3><p class="price">$120.00</p></article>
  <article class="product"><div class="product-media" style="--tone:#ece9e4;--tone2:#dcd8d1" role="img" aria-label="Off-white museum print shirt, folded"></div><div class="product-meta"><span>Solvane</span><span class="stars">★★★★★</span></div><h3>Dopo Designs Hero Graphic Tee</h3><p class="price">$240.00</p></article>
  <article class="product"><div class="product-media" style="--tone:var(--forest);--tone2:var(--stone)" role="img" aria-label="Green and grey camo hero shirt, folded"><span class="badge">-20%</span></div><div class="product-meta"><span>Solvane</span><span class="stars">★★★★★</span></div><h3>Bopo Designs Hero Graphic Tee</h3><p class="price"><s>$120.00</s><b>$150.00</b></p></article>
  <article class="product"><div class="product-media" style="--tone:#3a3a3a;--tone2:#555" role="img" aria-label="Charcoal city artwork shirt, folded"><span class="badge">-20%</span></div><div class="product-meta"><span>Solvane</span><span class="stars">★★★★★</span></div><h3>Dopo Designs Hero Graphic Tee</h3><p class="price"><s>$240.00</s><b>$120.00</b></p></article>
</div>

<section class="testimonial">
  <div class="testimonial-art" role="img" aria-label="Soft paper texture with faint orange, green and grey washes"></div>
  <div class="avatar" role="img" aria-label="Customer portrait"></div>
  <div class="quote" style="top:222px">“</div>
  <p>Duis autem vel eum iriure dolor in hendrerit in vulputate velit esse molestie consequat, vel illum dolore eu feugiat nulla facilisis at vero eros et accumsan et iusto odio dignissim qui blandit</p>
  <div class="quote" style="top:320px">”</div>
  <div class="arrow" style="left:153px"><svg width="28" height="28" viewBox="0 0 28 28"><path d="M18 14H10M13 10l-4 4 4 4" fill="none" stroke="#666" stroke-width="1.4"/></svg></div>
  <div class="arrow" style="left:1010px"><svg width="28" height="28" viewBox="0 0 28 28"><path d="M10 14h8M15 10l4 4-4 4" fill="none" stroke="#666" stroke-width="1.4"/></svg></div>
</section>

<section class="latest-head">
  <h2 class="section-title">LatestCreation</h2>
  <p>vulputate velit esse molestie consequat, vel illum dolore eu feugiat nulla</p>
</section>

<div class="grid" style="top:2276px">
  <article class="product"><div class="product-media" style="--tone:var(--clay);--tone2:var(--sand)" role="img" aria-label="Orange and sand hero shirt, folded"><span class="badge soft">-20%</span></div><div class="product-meta"><span>Solvane</span><span class="stars">★★★★★</span></div><h3>Ropo Designs Hero Graphic Tee</h3><p class="price"><s>$100.00</s><b class="cool">$80.00</b></p></article>
  <article class="product"><div class="product-media" style="--tone:var(--forest);--tone2:#4c6a55" role="img" aria-label="Dark green hero graphic shirt, folded"></div><div class="product-meta"><span>Solvane</span><span class="stars">★★★★★</span></div><h3>Dopo Designs Hero Graphic Tee</h3><p class="price">$240.00</p></article>
  <article class="product"><div class="product-media" style="--tone:var(--stone);--tone2:#a4a7a1" role="img" aria-label="Grey camo hero shirt, folded"></div><div class="product-meta"><span>Solvane</span><span class="stars">★★★★★</span></div><h3>Copo Designs Hero Graphic Tee</h3><p class="price">$240.00</p></article>
  <article class="product"><div class="product-media" style="--tone:#ece9e4;--tone2:#dcd8d1" role="img" aria-label="Off-white museum print shirt, folded"></div><div class="product-meta"><span>Solvane</span><span class="stars">★★★★★</span></div><h3>Bopo Designs Hero Graphic Tee</h3><p class="price">$120.00</p></article>
</div>

<section class="promo">
  <div class="promo-art" role="img" aria-label="Ceramic vases in pink and white with a bare branch"></div>
  <div class="promo-copy">
    <h2>30% Off</h2>
    <h3>Latest Ceramic Arts</h3>
    <p>There are latest ceramic arts, buy them within 15h dec2020 andyou will get a 30% discount</p>
    <span class="btn-solid">Shop Now</span>
  </div>
</section>

<section class="features">
  <div class="feature" style="left:245px">
    <svg width="30" height="30" viewBox="0 0 30 30" fill="none" stroke="#555" stroke-width="1.6"><path d="M28 2 2 13l10 4 4 10z M12 17 28 2"/></svg>
    <h4>FREE SHIPPING WORLDWIDE</h4>
    <p>Mirum est notare quam littera gothica, quam nunc putamus parum claram</p>
  </div>
  <div class="feature" style="left:490px">
    <svg width="30" height="30" viewBox="0 0 30 30"><text x="15" y="27" text-anchor="middle" font-family="Poppins,sans-serif" font-weight="600" font-size="30" fill="#555">$</text></svg>
    <h4>MONEY BACK GUARANTEE</h4>
    <p>Mirum est notare quam littera gothica, quam nunc putamus parum claram</p>
  </div>
  <div class="feature" style="left:736px">
    <svg width="30" height="30" viewBox="0 0 30 30" fill="none" stroke="#555"><circle cx="15" cy="15" r="12" stroke-width="3"/><circle cx="15" cy="15" r="5" stroke-width="2"/><path d="M6 6l5 5M24 6l-5 5M6 24l5-5M24 24l-5-5" stroke-width="3"/></svg>
    <h4>ONLINE SUPPORT 24/7</h4>
    <p>Mirum est notare quam littera gothica, quam nunc putamus parum claram</p>
  </div>
</section>
<div class="rule" style="top:3175px;left:205px;width:794px"></div>

<section class="newsletter">
  <div class="eyebrow">Special Offers For Subscribers</div>
  <h2>Ten Percent Member Discount</h2>
  <p>Subscribe to our newsletters now and stay up to date with new collections, the latest lookbooks and exclusive offers.</p>
  <div class="signup"><span>Email Address</span><b>SUBSCRIBE</b></div>
</section>

<footer class="site-footer">
  <div class="footer-rule" style="top:13px"></div>
  <div class="logo">Ateliervoransol</div>
  <p class="about">There are many variations of passages of look even slightly believable.</p>
  <div class="social"><i></i><i></i><i></i><i></i><i></i></div>
  <ul class="col" style="left:480px"><h5>Information</h5><li>About Us</li><li>Delivery Information</li><li>Privacy Policy</li><li>Terms &amp; Conditions</li><li>Site Map</li></ul>
  <ul class="col" style="left:657px"><h5>Extras</h5><li>Brands</li><li>Gift Certificates</li><li>Affiliate</li><li>Specials</li><li>Contact Us</li></ul>
  <ul class="col" style="left:818px"><h5>Store Information</h5>
    <li><svg width="9" height="10" viewBox="0 0 9 10"><path d="M4.5 0a3.5 3.5 0 0 0-3.5 3.5C1 6 4.5 10 4.5 10S8 6 8 3.5A3.5 3.5 0 0 0 4.5 0z" fill="#fff"/><circle cx="4.5" cy="3.5" r="1.2" fill="#111"/></svg>Ardoise - Art Store</li>
    <li class="indent">United States</li>
    <li><svg width="9" height="10" viewBox="0 0 9 10"><path d="M1 1l2-1 1.5 3-1 1c.6 1.3 1.4 2.1 2.5 2.5l1-1 3 1.5-1 2C4 9 0 5 1 1z" fill="#fff"/></svg>000-000-0000</li>
    <li><svg width="9" height="10" viewBox="0 0 9 10"><rect x="0" y="3" width="9" height="6" fill="#fff"/><rect x="2" y="0" width="5" height="4" fill="#fff"/></svg>123456</li>
    <li><svg width="9" height="10" viewBox="0 0 9 10"><rect x=".5" y="2" width="8" height="6" fill="none" stroke="#fff"/><path d="M.5 2 4.5 5.5 8.5 2" fill="none" stroke="#fff"/></svg>hello@ateliervoransol.ca</li>
  </ul>
  <div class="footer-rule" style="top:208px"></div>
  <div class="copyright">© 2020, All rights Reserved, Ateliervoransol</div>
  <div class="cards"><i></i><i></i><i></i><i></i><i></i></div>
</footer>

</body>
</html>
```